Need wine label for brand that is named: Tolmesha Vineyards & Winery

Tolmesha is a yoga way of breathing. In Sanskrit Tolmesha means "flying up." I would like a creative wine label that articulates Tolmesha. The label should include a graphic and the name Tolmesha on one line and Vineyards & Winery in smaller print underneath Tolmesha.

```html
<!DOCTYPE html>
<html lang="en">
<head>
<meta charset="utf-8">
<title>Tolmesha Vineyards &amp; Winery — Pinot Noir Label</title>
<link rel="stylesheet" href="https://fonts.googleapis.com/css2?family=Cinzel:wght@400;500&family=Oswald:wght@300&family=Jost:wght@600&display=swap">
<style>
  :root {
    --label-bg-top: #151619;
    --label-bg-mid: #232428;
    --label-bg-bottom: #141518;
    --brand-pink: #c63a8f;
    --text-silver: #c4c4c6;
    --text-white: #f4f4f4;
    --band-red: #ff3d4f;
    --band-pink: #e8306f;
    --band-purple: #8e4fb8;
    --band-teal: #3ab7c4;
    --band-blue: #3a6fe0;
  }
  * { margin: 0; padding: 0; box-sizing: border-box; }
  html, body {
    width: 943px;
    height: 1200px;
    overflow: hidden;
    background: var(--label-bg-top);
  }
  .wine-label {
    position: relative;
    width: 943px;
    height: 1200px;
    background: linear-gradient(180deg, var(--label-bg-top) 0%, var(--label-bg-mid) 55%, var(--label-bg-bottom) 100%);
    overflow: hidden;
  }
  .ornament-band {
    position: absolute;
    top: 0;
    width: 63px;
    height: 1200px;
    background: linear-gradient(180deg, var(--band-red) 0%, var(--band-pink) 30%, var(--band-purple) 62%, var(--band-teal) 86%, var(--band-blue) 100%);
  }
  .ornament-band--left { left: 66px; }
  .ornament-band--right { left: 815px; }
  .label-text {
    position: absolute;
    left: 0;
    width: 943px;
    text-align: center;
    white-space: nowrap;
  }
  .brand-name {
    top: 82px;
    font-family: "Cinzel", serif;
    font-weight: 500;
    font-size: 70px;
    letter-spacing: 0.06em;
    color: var(--brand-pink);
    line-height: 1;
  }
  .brand-descriptor {
    top: 230px;
    font-family: "Cinzel", serif;
    font-weight: 400;
    font-size: 25px;
    letter-spacing: 0.16em;
    color: var(--text-silver);
    line-height: 1;
  }
  .varietal {
    top: 430px;
    font-family: "Oswald", sans-serif;
    font-weight: 300;
    font-size: 68px;
    letter-spacing: 0.1em;
    color: var(--text-silver);
    line-height: 1;
  }
  .vintage {
    top: 680px;
    font-family: "Jost", sans-serif;
    font-weight: 600;
    font-size: 54px;
    letter-spacing: 0.2em;
    color: var(--text-white);
    line-height: 1;
  }
  .collection {
    top: 800px;
    font-family: "Oswald", sans-serif;
    font-weight: 300;
    font-size: 50px;
    letter-spacing: 0.2em;
    color: var(--text-white);
    line-height: 1;
  }
  .appellation {
    top: 922px;
    font-family: "Jost", sans-serif;
    font-weight: 600;
    font-size: 44px;
    letter-spacing: 0.16em;
    color: var(--text-white);
    line-height: 1;
  }
  .alcohol {
    top: 1142px;
    font-family: "Oswald", sans-serif;
    font-weight: 300;
    font-size: 25px;
    letter-spacing: 0.16em;
    color: var(--text-silver);
    line-height: 1;
  }
</style>
</head>
<body>
  <main class="wine-label">
    <div class="ornament-band ornament-band--left" role="img" aria-label="Vertical ornamental mandala border fading from red through purple to blue"></div>
    <div class="ornament-band ornament-band--right" role="img" aria-label="Vertical ornamental mandala border fading from red through purple to blue"></div>

    <h1 class="label-text brand-name">Tolmesha</h1>
    <p class="label-text brand-descriptor">Vineyards &amp; Winery</p>

    <h2 class="label-text varietal">PINOT NOIR</h2>
    <p class="label-text vintage">2014</p>
    <p class="label-text collection">COLLECTION</p>
    <p class="label-text appellation">Napa Valley</p>
    <p class="label-text alcohol">11.8% alc/vol.</p>
  </main>
</body>
</html>
```